Beacon Stewards Brochure Design*

We host a local leadership development program every two years. We need a brochure to promote the program. We would like it to be 8 1/2 x 11, tri-fold. I have attached a Word document with the necessary info for the brochure. The brochure will be professionally printed. We would like the final design to be in InDesign.

Target Market(s)

Potential participants of our leadership program. They will be local leaders, male and female, from 30-60 years of age.

Requirements
Must have
• Content as detailed in the Word document attached. Our logo.
Nice to have
• A design that is attractive to young professionals.

```html
<!DOCTYPE html>
<html lang="en">
<head>
<meta charset="utf-8">
<title>Beacon Stewards – Tri-fold Brochure</title>
<link rel="stylesheet" href="https://fonts.googleapis.com/css2?family=Montserrat:wght@300;600;700&family=Open+Sans:wght@400;600;700&display=swap">
<style>
  :root {
    --sky: #2a9fd8;
    --navy: #2e3282;
    --orange: #f28c24;
    --ink: #1d1f3d;
    --paper: #ffffff;
    --backdrop: #e6e7e8;
    --shadow-grey: #e2e3e5;
    --photo-warm-a: #9a8466;
    --photo-warm-b: #4f4640;
    --portrait-a: #9c9c9c;
    --portrait-b: #4a4a4a;
  }
  * { margin: 0; padding: 0; box-sizing: border-box; }
  html, body { width: 1200px; height: 1000px; overflow: hidden; background: var(--backdrop); }
  .canvas { position: relative; width: 1200px; height: 1000px; }
  .artwork { position: absolute; inset: 0; }
  .copy {
    position: absolute;
    font-family: "Open Sans", Arial, sans-serif;
    font-size: 11px;
    line-height: 18.2px;
    color: var(--ink);
  }
  .copy strong { font-weight: 700; }
  .testimonials-heading {
    position: absolute; left: 127px; top: 157px;
    font-family: "Montserrat", Arial, sans-serif;
    font-weight: 700; font-size: 16.5px; line-height: 20px; color: var(--paper);
  }
  .testimonial-terri { left: 127px; top: 207px; }
  .testimonial-evan-lead { left: 149px; top: 598px; }
  .testimonial-evan-end { left: 589px; top: 574px; }
  .footnote { left: 570px; top: 784px; font-size: 9px; line-height: 15px; }
  .brand-name {
    position: absolute; left: 800px; top: 150px;
    font-family: "Montserrat", Arial, sans-serif;
    font-weight: 700; font-size: 17px; color: var(--navy);
    display: flex; align-items: center; gap: 8px;
  }
  .brand-name .mark { width: 14px; height: 14px; border-radius: 50%; background: var(--sky); }
  .pull-quote {
    position: absolute; left: 800px; top: 511px;
    font-family: "Montserrat", Arial, sans-serif;
    font-weight: 300; font-size: 20.5px; line-height: 29px; color: var(--paper);
  }
  .sponsors { position: absolute; left: 799px; top: 764px; font-family: "Open Sans", Arial, sans-serif; }
  .sponsors h3 { font-size: 15px; font-weight: 700; color: var(--sky); line-height: 20px; margin-bottom: 2px; }
  .sponsors p { font-size: 13px; line-height: 20px; color: var(--navy); }
</style>
</head>
<body>
<main class="canvas">
  <svg class="artwork" width="1200" height="1000" viewBox="0 0 1200 1000" aria-hidden="false">
    <defs>
      <linearGradient id="group-photo-tone" x1="0" y1="0" x2="1" y2="1">
        <stop offset="0" stop-color="var(--photo-warm-a)"/>
        <stop offset="1" stop-color="var(--photo-warm-b)"/>
      </linearGradient>
      <linearGradient id="portrait-tone" x1="0" y1="0" x2="0" y2="1">
        <stop offset="0" stop-color="var(--portrait-a)"/>
        <stop offset="1" stop-color="var(--portrait-b)"/>
      </linearGradient>
    </defs>

    <!-- brochure sheet -->
    <rect class="sheet" x="79" y="89" width="1041" height="803" fill="var(--paper)"/>

    <!-- left panel: offset grey plate and blue testimonial card -->
    <path class="card-plate" d="M153 190 H426 V548 H175 Q153 548 153 526 Z" fill="var(--shadow-grey)"/>
    <path class="card-blue" d="M79 141 H377 Q399 141 399 163 V512 H101 Q79 512 79 490 Z" fill="var(--sky)"/>
    <path class="portrait-terri" role="img" aria-label="Portrait of alumna Dana Whitfield"
          d="M301 203 H399 V329 H279 V225 Q279 203 301 203 Z" fill="url(#portrait-tone)" stroke="var(--navy)" stroke-width="2"/>
    <path class="card-orange" d="M147 573 H426 V892 H147 Q125 892 125 870 V595 Q125 573 147 573 Z" fill="var(--orange)"/>

    <!-- centre / right panels: waves, group photo, navy field -->
    <path class="wave-top" d="M426 218 H870 C910 218 925 168 965 168 H1120 V180 H968 C932 180 917 232 875 232 H426 Z" fill="var(--sky)"/>
    <path class="group-photo" role="img" aria-label="Group photo of program alumni standing together in a meeting room"
          d="M426 232 H875 C917 232 932 180 968 180 H1120 V470 H640 C600 470 595 520 555 520 H426 Z" fill="url(#group-photo-tone)"/>
    <path class="wave-mid" d="M426 520 H555 C595 520 600 470 640 470 H1120 V484 H645 C608 484 600 532 560 532 H426 Z" fill="var(--sky)"/>
    <path class="wave-orange" d="M426 728 H760 C790 728 795 688 830 688 H985 C1020 688 1025 728 1060 728 H1120 V746 H1055 C1015 746 1012 704 980 704 H835 C805 704 800 746 765 746 H426 Z" fill="var(--orange)"/>
    <path class="navy-field" d="M426 532 H560 C600 532 608 484 645 484 H1120 V728 H1060 C1025 728 1020 688 985 688 H830 C795 688 790 728 760 728 H426 Z" fill="var(--navy)"/>

    <!-- quote marks -->
    <g class="quote-marks" fill="var(--sky)">
      <path d="M801 503 V493 Q801 485 809 483 L811 487 Q806 489 806 493 H811 V503 Z"/>
      <path d="M815 503 V493 Q815 485 823 483 L825 487 Q820 489 820 493 H825 V503 Z"/>
    </g>
    <g class="quote-marks-close" fill="var(--orange)">
      <path d="M802 664 H811 V674 Q811 682 803 684 L801 680 Q806 678 806 674 H802 Z"/>
      <path d="M816 664 H825 V674 Q825 682 817 684 L815 680 Q820 678 820 674 H816 Z"/>
    </g>

    <!-- second testimonial card -->
    <path class="portrait-evan" role="img" aria-label="Portrait of alumnus Evan T. Rowley"
          d="M474 563 H570 V690 H452 V585 Q452 563 474 563 Z" fill="url(#portrait-tone)" stroke="var(--orange)" stroke-width="2"/>
    <path class="card-orange-small" d="M570 562 H727 Q747 562 747 582 V773 H590 Q570 773 570 753 Z" fill="var(--orange)"/>
  </svg>

  <h2 class="testimonials-heading">What Community<br>alumni are saying</h2>

  <p class="copy testimonial-terri">
    “Beacon Stewards was<br>an awesome experience! I<br>learned many interesting<br>things about the county that<br>I have lived in all my life.<br>We had very informative<br>panel discussions and the<br>tours of local attractions, including the Millbrook<br>Correctional Facility were eye opening! I enjoyed<br>learning and working beside a great group of<br>folks who are taking leadership roles in our<br>communities to make our county a better place<br>to live, work and play.”<br>
    <strong>Dana Whitfield</strong><br>Co-Owner, Harbor Smokehouse
  </p>

  <p class="copy testimonial-evan-lead">
    “For the first year and a half I was working at R.<br>Hollis Grant, I commuted from Bayview,<br>so I was not involved in the community at all.<br>Once we moved here, I knew I wanted and felt I<br>had to become more involved. I learned about<br>the program through a colleague. I couldn’t have<br>asked for a better experience and it really exposed<br>me to the many ways that I could get involved and<br>contribute to the chamber and our community.<br>I didn’t know a soul in that 2014 class when it<br>started and now many of them are my very best<br>friends. If you have an opportunity to go through<br>Beacon Stewards you would be crazy to pass
  </p>

  <p class="copy testimonial-evan-end">
    it up. It is the best program<br>the Chamber has and, quite<br>frankly, one of the best<br>opportunities to better<br>yourself in this community.<br>
    <strong>Evan T. Rowley</strong><br>CPA, Partner/Manager of<br>the Fairhaven Office<br>R. Hollis Grant &amp;<br>Associates, LLP
  </p>

  <p class="copy footnote">*We may want to have one or two more<br>testimonials if needed.</p>

  <div class="brand-name"><span class="mark"></span>Beacon Stewards</div>

  <p class="pull-quote">The greatest wealth of a<br>community lies not in the<br>amount of its treasure,<br>but in the quality of its<br>leadership.</p>

  <section class="sponsors">
    <h3>Sponsored by:</h3>
    <p>Northbridge Community College<br>Lakemont Chamber of Commerce and<br>Tourism</p>
  </section>
</main>
</body>
</html>
```